Real Estate Web Page Redesign

We are a small town real estate agency in need of a web site redesign. To give you a little background on our agency…our target is middle income households and farmers. Our staff includes real estate agents and an auctioneer. We’ve been in business since 1997. We handle residential, commercial, recreational land and farmland.
Our current web site design is outdated and needs a more modern look. We are open to all design ideas but would want them to reflect our small town rural tradition and heritage.
The functionality and features of the site will remain the same. Your design will have to accommodate the existing features on the site. I have a programmer who will take the design you provide and retrofit the existing site functionality with it.
The deliverable will be a .psd file that can be converted to html for a site template. (We will do the conversion.)
The existing site is at:
http://www.tomwendelproperties.example/home.asp
Please take time to visit the site and note the current functionality the site has: property search, real estate news feed, mortgage rate feed, listings, navigation bar will need to handle existing links and expand to handle other future page links. The template provided will need to accommodate these features.
The current page logo can be used in the design or we are open to a redesign of that as well if needed to go with the design better.
Updates
Target Market(s)
Middle income households and farmers looking for the services of a real estate agent or auctioneer.
Industry/Entity Type
Real Estate
Look and feel
Each slider illustrates characteristics of the customer's brand and the style your logo design should communicate.

```html
<!DOCTYPE html>
<html lang="en">
<head>
<meta charset="utf-8">
<title>Wendel Real Estate and Land Company</title>
<link href="https://fonts.googleapis.com/css2?family=PT+Sans:wght@400;700&family=Arimo:wght@400;700&display=swap" rel="stylesheet">
<style>
:root{
  --page:#efefef;
  --white:#ffffff;
  --blue:#3d6f9e;
  --blue-dark:#2c5a85;
  --blue-bar:#4c7ba1;
  --sky-top:#5f8fc6;
  --sky-low:#c9dcef;
  --orange:#f26b10;
  --orange-light:#ff9a3c;
  --text:#444444;
  --muted:#666666;
  --line:#dddddd;
  --table-head:#3f6f97;
}
*{box-sizing:border-box;margin:0;padding:0}
html,body{width:988px;height:1200px;overflow:hidden;background:var(--page);font-family:"Arimo",Arial,sans-serif;color:var(--text)}
.page{position:relative;width:988px;height:1200px}
.site{position:absolute;left:165px;top:8px;width:658px;height:1095px;background:var(--white);border-radius:6px;box-shadow:0 0 8px rgba(0,0,0,.18)}
.abs{position:absolute}
.brand{left:10px;top:12px;display:flex;align-items:center;gap:8px}
.brand-mark{width:24px;height:24px;background:var(--blue);border-radius:3px}
.brand-name{font-family:"PT Sans",sans-serif;font-weight:700;font-size:20px;line-height:21px;color:var(--blue)}
.phone{right:12px;top:14px;font-size:12px;color:var(--muted)}
.phone b{font-size:15px;color:#1e6bb8;margin-left:4px}
.nav{right:6px;top:50px;display:flex;gap:3px}
.nav a{display:block;height:25px;padding:0 11px;line-height:25px;font-size:10.5px;color:#3a6a98;text-decoration:none;background:linear-gradient(#fff,#e8e8e8);border:1px solid #cfcfcf;border-bottom:none;border-radius:3px 3px 0 0}
.nav a.active{background:var(--blue);color:#fff;border-color:var(--blue);padding:0 16px}
.hero{left:0;top:74px;width:658px;height:338px;background:linear-gradient(var(--sky-top),var(--sky-low) 55%,#eef2f5 90%,#f2f2f2)}
.hero-title{left:20px;top:10px;font-size:31px;color:#fff;letter-spacing:-.3px}
.hero-photo{left:0;top:58px;width:430px;height:190px;background:linear-gradient(180deg,#b7cbe0,#d9d3c4 55%,#7fa85a)}
.quote-arrow{left:-2px;top:224px}
.search{left:450px;top:132px;width:228px;height:255px;background:var(--blue);border-radius:4px;padding:8px}
.search-inner{background:#fff;height:100%;border-radius:2px;padding:6px 12px}
.search h2{font-family:"PT Sans",sans-serif;font-weight:400;font-size:18px;color:var(--blue)}
.search h2 b{color:var(--blue-dark)}
.search label{display:block;font-size:9px;font-weight:700;margin-top:8px;color:#333}
.select{margin-top:3px;height:18px;border:1px solid #ccc;border-radius:2px;font-size:8px;color:#777;padding:4px 8px;position:relative;background:linear-gradient(#fff,#f1f1f1)}
.select::after{content:"";position:absolute;right:6px;top:7px;border:3px solid transparent;border-top-color:#666}
.btn-quote{margin-top:12px;height:32px;border-radius:3px;background:linear-gradient(var(--orange-light),var(--orange));color:#fff;font-family:"PT Sans",sans-serif;font-weight:700;font-size:16px;text-align:center;line-height:32px}
.welcome-bar{left:6px;top:413px;width:656px;height:38px;background:var(--blue-bar);color:#fff;font-family:"PT Sans",sans-serif;font-size:18px;line-height:38px;padding-left:10px}
.panel{border:1px solid var(--line);border-radius:3px;background:#fff}
.welcome-text{left:10px;top:451px;width:648px;height:94px;padding:8px 7px;font-size:8.2px;line-height:12px;color:var(--muted)}
.heading{font-family:"PT Sans",sans-serif;font-size:19px;color:#111}
.cards{left:9px;top:596px;width:423px;height:224px;display:flex;padding:3px}
.card{flex:1;padding:4px 6px;border-right:1px solid #eee;position:relative;font-size:8px;color:var(--muted)}
.card:last-child{border:none}
.card h3{font-size:8px;font-weight:700;color:#222;text-decoration:underline}
.card .loc{margin:2px 0 3px}
.card .photo{height:72px;border:1px solid #999}
.card .beds{margin-top:8px;font-weight:700;color:#222}
.card .price{font-weight:700;color:#222}
.card .price span{color:var(--orange)}
.card p{margin-top:4px;line-height:11px}
.btn-small{position:absolute;display:block;background:var(--orange);color:#fff;font-size:8px;font-weight:700;padding:4px 10px}
.card .btn-small{left:-4px;bottom:6px}
.rates{left:439px;top:596px;width:219px;height:150px;padding:3px}
table{border-collapse:collapse;width:100%;font-size:8.5px}
th{background:var(--table-head);color:#fff;text-align:left;padding:7px 7px;border:1px solid #fff}
td{padding:6px 7px;border:1px solid #e2e2e2;color:#555}
td:nth-child(2){background:#f4f4f4}
.calc{margin:8px 2px;font-size:9px;font-weight:700;color:var(--orange);text-decoration:underline;display:flex;align-items:center;gap:8px}
.calc i{width:11px;height:12px;border:1px solid #8aa;background:#e8eef2;display:block}
.subscribe{left:439px;top:786px;width:219px;height:41px;padding:9px 5px;display:flex;justify-content:space-between;align-items:center}
.subscribe .field{width:124px;height:18px;border:1px solid #ddd;font-size:8px;font-weight:700;padding:4px;color:#222}
.subscribe .btn-submit{width:72px;height:23px;border-radius:3px;background:linear-gradient(var(--orange-light),var(--orange));color:#fff;font-family:"PT Sans",sans-serif;font-weight:700;font-size:13px;text-align:center;line-height:23px}
.agents{left:9px;top:866px;width:423px;height:229px;padding:10px 8px;font-size:8.3px;line-height:12px;color:var(--muted)}
.step{margin-top:10px;border-top:1px solid #f0f0f0;padding-top:8px}
.step h4{font-size:8px;color:#222;text-decoration:underline;display:flex;gap:6px;align-items:center}
.step h4 i{width:11px;height:9px;background:#e7c55a;display:block}
.step p{margin-top:4px}
.agents .btn-small{left:3px;bottom:12px}
.news{left:439px;top:866px;width:219px;height:229px;padding:8px}
.item{display:flex;gap:10px;padding:3px 0 14px;border-bottom:1px solid #eee;margin-bottom:8px;font-size:8.3px;line-height:11px}
.date{width:22px;height:34px;flex:none;border-radius:3px;background:linear-gradient(#ffb34a,#f28a10);border:1px solid #c66e0b;color:#fff;text-align:center;font-size:14px;font-weight:700;line-height:16px}
.date small{display:block;font-size:8px;font-style:italic;font-weight:400;color:#7a3a00}
.item h5{font-size:8.3px;color:#222;text-decoration:underline}
.news .btn-small{left:0;bottom:10px}
.footer{left:177px;top:1137px;width:646px;font-size:8.5px;color:#555}
.footer-nav{position:absolute;right:0;top:0}
.footer-nav a{color:#555;text-decoration:none;margin:0 4px}
.disclaimer{left:175px;top:1152px;width:650px;border-top:1px solid #ccc;padding-top:6px;font-size:8.3px;line-height:12px;color:#666}
.disclaimer b{font-weight:400;font-size:10px;color:#333}
</style>
</head>
<body>
<div class="page">
  <div class="site">
    <div class="abs brand"><span class="brand-mark"></span><div class="brand-name">WENDEL REAL ESTATE<br>AND LAND COMPANY</div></div>
    <div class="abs phone">Call us: <b>1-800-555-0142</b></div>
    <nav class="abs nav"><a class="active">Home</a><a>About Us</a><a>Open Houses</a><a>Calculator</a><a>Contact Us</a></nav>

    <section class="abs hero">
      <div class="abs hero-title">Rates you can afford, Providers you can trust</div>
      <div class="abs hero-photo" role="img" aria-label="Family standing in front of a suburban house"></div>
      <svg class="abs quote-arrow" width="440" height="112" viewBox="0 0 440 112">
        <defs><linearGradient id="arrowFill" x1="0" y1="0" x2="0" y2="1"><stop offset="0" stop-color="#ff8a2a"/><stop offset="1" stop-color="#e85d05"/></linearGradient></defs>
        <path d="M0 20 H390 V0 L437 58 L390 112 V92 H0 Z" fill="url(#arrowFill)"/>
        <text x="24" y="70" font-family="PT Sans, sans-serif" font-weight="700" font-size="30" fill="#fff">Get a FREE Quote Now!</text>
      </svg>
    </section>

    <form class="abs search">
      <div class="search-inner">
        <h2>Search <b>OUR LISTING</b></h2>
        <label>Property Type:</label><div class="select">Select</div>
        <label>Number of Bedrooms:</label><div class="select">Select</div>
        <label>City</label><div class="select">Select</div>
        <label>Price</label><div class="select">Select</div>
        <div class="btn-quote">Get Quote</div>
      </div>
    </form>

    <h1 class="abs welcome-bar">Welcome to&nbsp; Wendel Real Estate and Land Company</h1>
    <div class="abs panel welcome-text">Welcome to Wendel Real Estate and Land Company's web site. Your visit here will make it easy for you to find the real estate you are seeking by using our simple search menu. Not only will you find area real estate listings, but also other items such as the latest mortgage rates and real estate news, and businesses that are associated with buying and selling homes and farmland. I will be servicing the needs of the people in the Alder Creek, Millbrook, Pine Ridge, Oakdale, Fairfield and all area communities. I have been in the real estate business since 1997 and have been a broker since 1999. I'm looking forward to marketing your property for "top dollar" or finding that "perfect" piece of property you desire whether it be residential, commercial, recreational, farmland (statewide), country property, or 1031 exchange. I am also a member of the Central Prairie Multiple Listing Service.</div>

    <h2 class="abs heading" style="left:17px;top:560px">Our Best Proposals</h2>
    <div class="abs panel cards">
      <article class="card"><h3>NASCET RIDULS DUSGIAT</h3><div class="loc">( New-York)</div><div class="photo" role="img" aria-label="Modern house lit at dusk" style="background:linear-gradient(#2a4a7a,#c08a40)"></div><div class="beds">6 BEDS</div><div class="price">PRICE: <span>$300000</span></div><p>Lorem ipsum dolor sit amet, consectetur adipisicing elit, sed do eiusmod tempor incididunt ut</p><a class="btn-small">DETAILS</a></article>
      <article class="card"><h3>NASCET RIDULS DUSGIAT</h3><div class="loc">( Los-Angeles )</div><div class="photo" role="img" aria-label="Waterfront villa at twilight" style="background:linear-gradient(#3a68a8,#e0a050 60%,#2a4f80)"></div><div class="beds">5 BEDS</div><div class="price">PRICE: <span>$299000</span></div><p>Lorem ipsum dolor sit amet, consectetur adipisicing elit, sed do eiusmod tempor incididunt ut</p><a class="btn-small">DETAILS</a></article>
      <article class="card"><h3>NASCET RIDULS DUSGIAT</h3><div class="loc">( Washington )</div><div class="photo" role="img" aria-label="Two-storey family house with garage" style="background:linear-gradient(#a9c6e6,#b9a88e 60%,#6f8a4c)"></div><div class="beds">6 BEDS</div><div class="price">PRICE: <span>$315000</span></div><p>Lorem ipsum dolor sit amet, consectetur adipisicing elit, sed do eiusmod tempor incididunt ut</p><a class="btn-small">DETAILS</a></article>
    </div>

    <h2 class="abs heading" style="left:441px;top:560px">Mortgage Rates</h2>
    <div class="abs panel rates">
      <table>
        <tr><th>Loan Type</th><th>Rates</th><th>APR</th><th>Points</th></tr>
        <tr><td>30 Year fixed</td><td>5 %</td><td>5.16 %</td><td>1.000 %</td></tr>
        <tr><td>30 Year Tres</td><td>5.3 %</td><td>3.79 %</td><td>2.375 %</td></tr>
        <tr><td>15 Year fixed</td><td>3.6 %</td><td>3.89 %</td><td>1.000 %</td></tr>
        <tr><td>Fed Prime</td><td>4 %</td><td>4.15 %</td><td>1.375 %</td></tr>
      </table>
      <div class="calc"><i></i>Mortgage Calculator</div>
    </div>

    <h2 class="abs heading" style="left:441px;top:753px">Subscribe</h2>
    <div class="abs panel subscribe"><div class="field">Enter your e-mail here:</div><div class="btn-submit">Submit</div></div>

    <h2 class="abs heading" style="left:17px;top:834px">Choosing the Real Estate Listing Agents</h2>
    <div class="abs panel agents">
      <p>Lorem ipsum dolor sit amet, consectetur adipisicing elit, sed do eiusmod tempor incididunt ut labore et dolore magna aliqua. Ut enim ad minim veniam, quis nostrud exercitation ullamco laboris nisi ut aliquip ex ea commodo consequat.</p>
      <div class="step"><h4><i></i>CREATE A LOAN REQUEST</h4><p>Dolor sit amet, consectetur adipisicing elit, sed do eiusmod tempor incididunt ut labore et dolore</p></div>
      <div class="step"><h4><i></i>RECEIVE QUOTES</h4><p>Sit amet, consectetur adipisicing elit, sed do eiusmod tempor</p></div>
      <div class="step"><h4><i></i>CONTACT THE LENDER</h4><p>Dolor sit amet, consectetur adipisicing elit, sed do eiusmod tempor incididunt ut labore et dolore</p></div>
      <a class="btn-small">DETAILS</a>
    </div>

    <h2 class="abs heading" style="left:441px;top:834px">Latest News</h2>
    <div class="abs panel news">
      <div class="item"><div class="date">30<small>Jan</small></div><div><h5>Hendre maurs phauselus</h5>Varuusm cumsociis natoqe amet penatibus cursusdui</div></div>
      <div class="item"><div class="date">30<small>Jan</small></div><div><h5>Hendre maurs phauselus</h5>Varuusm cumsociis natoqe amet penatibus cursusdui</div></div>
      <div class="item"><div class="date">30<small>Jan</small></div><div><h5>Hendre maurs phauselus</h5>Varuusm cumsociis natoqe amet penatibus cursusdui</div></div>
      <a class="btn-small">ALL NEWS</a>
    </div>
  </div>

  <footer class="abs footer">Copyright © 2011 www.wendelrealestate.example.
    <span class="footer-nav"><a>Home</a>|<a>About Us</a>|<a>Privacy Policy</a>|<a>Terms of Use</a></span>
  </footer>
  <div class="abs disclaimer"><b>DISCLAIMER:</b> Lorem ipsum dolor sit amet, consectetuer adipiscing elit, sed diam nonummy nibh euismod tincidunt ut laoreet dolore magna aliquam erat volutpat. Ut wisi enim ad minim veniam, quis nostrud exerci tation ullamcorper</div>
</div>
</body>
</html>
```